Holistic Therapy (aromatherapy, massage, reflexology, life coaching, soul healing, aura reading)

I work for myself as a holistic therapist doing: aromatherapy massage, massage, reflexology, abdominal-sacral massage, life coaching, soul healing, aura readings. I want a business card that doesn't focus on any one of these( so not just feet or a massage couch,but rather a card that creates the feeling of wholeness, healing, health and which can encompass all my therapies - e.g. green or purple are colours I like (especially green, or maybe green on back and purple on front). It's going to be called Rosa Pell Therapies. I don't want to list all my therapies on the card in case I add others later.). At some point I will create a website but in this instance I just want to get some cards printed to get 'out there' while I design my website.

Hi, thanks for all your designs. Can you find a way to include the therapies that I offer within the card, either on the front or back…the therapies I offer are: aromatherapy massage, reflexology, swedish body massage, abdominal-sacral massage, nutrition, soul healing, aura readings. (Maybe have them with a bullet point before each?) I am not sure whether they should be on the front of the card or the back or whether having them would spoil the card but it occurred to me that just having rosa pell therapies doesn't tell people what therapies I offer, hence the new idea to list them somehow…)

Target Market(s)

Mainly women (middle class probably with disposable incomes).

Industry/Entity Type

Massage

Contact Information for Business Card

Rosa Pell Therapies, Tel: 07700 900482, email: lumacrest@postvane.com, (on back of card I want: Rosalind Pell BScHons, CPWRA, RGPC.)

Requirements
Nice to have
• A logo for Rosa Pell Therapies would be good.

```html
<!DOCTYPE html>
<html lang="en">
<head>
<meta charset="utf-8">
<title>Rosa Pell Therapies – Business Card</title>
<link rel="stylesheet" href="https://fonts.googleapis.com/css2?family=Mulish:wght@400;700&display=swap">
<style>
  :root {
    --page: #ffffff;
    --card: #ffffff;
    --green: #3cb64a;
    --green-light: #6cc94a;
    --green-dark: #1fa33f;
    --purple: #b985b8;
    --purple-light: #e6d2e6;
    --ink: #1f1f1f;
    --icon: #3a3a3a;
  }
  * { box-sizing: border-box; margin: 0; padding: 0; }
  html, body {
    width: 968px; height: 1200px; overflow: hidden;
    background: var(--page);
    font-family: "Mulish", "Century Gothic", sans-serif;
  }
  .canvas { position: relative; width: 968px; height: 1200px; }
  .card {
    position: absolute;
    width: 788px; height: 468px;
    background: var(--card);
    border-radius: 24px;
    overflow: hidden;
    box-shadow: 0 8px 14px rgba(0,0,0,0.28), 0 0 2px rgba(0,0,0,0.15);
  }
  .card--front { left: 79px; top: 57px; }
  .card--back { left: 85px; top: 648px; }
  .card__swoosh { position: absolute; inset: 0; width: 100%; height: 100%; }

  .brand { position: absolute; display: flex; align-items: center; }
  .brand__dot { border-radius: 50%; background: var(--purple); flex: none; }
  .brand__name { color: var(--green); font-weight: 700; white-space: nowrap; }

  .brand--front { left: 92px; top: 172px; gap: 22px; }
  .brand--front .brand__dot { width: 78px; height: 78px; }
  .brand--front .brand__name { font-size: 44px; }

  .brand--back { right: 40px; top: 344px; gap: 12px; }
  .brand--back .brand__dot { width: 36px; height: 36px; }
  .brand--back .brand__name { font-size: 21px; }

  .holder {
    position: absolute; left: 193px; top: 98px;
    font-size: 22px; font-weight: 700; color: var(--ink);
  }
  .contact { position: absolute; left: 193px; display: flex; align-items: center; gap: 12px; color: var(--ink); font-size: 22px; }
  .contact--phone { top: 192px; font-weight: 700; }
  .contact--email { top: 240px; font-weight: 400; }
  .contact__icon { width: 28px; height: 28px; flex: none; }
</style>
</head>
<body>
<div class="canvas">

  <section class="card card--front">
    <svg class="card__swoosh" viewBox="0 0 723 430" preserveAspectRatio="none" aria-hidden="true">
      <defs>
        <linearGradient id="front-purple" x1="0" y1="0" x2="1" y2="0">
          <stop offset="0.15" stop-color="#ffffff"/>
          <stop offset="0.55" stop-color="#dcc0dc"/>
          <stop offset="0.8" stop-color="#b985b8"/>
        </linearGradient>
      </defs>
      <path d="M60 428 C 300 420, 560 380, 723 145 L723 185 C 580 398, 320 425, 60 430 Z" fill="var(--green)"/>
      <path d="M60 430 C 330 428, 600 400, 723 198 L723 430 Z" fill="url(#front-purple)"/>
    </svg>
    <div class="brand brand--front">
      <span class="brand__dot"></span>
      <span class="brand__name">Rosa Pell Therapies</span>
    </div>
  </section>

  <section class="card card--back">
    <svg class="card__swoosh" viewBox="0 0 723 430" preserveAspectRatio="none" aria-hidden="true">
      <defs>
        <linearGradient id="back-green" x1="0" y1="0" x2="1" y2="0">
          <stop offset="0" stop-color="#22a93f"/>
          <stop offset="0.6" stop-color="#6cc94a"/>
        </linearGradient>
      </defs>
      <path d="M0 145 C 150 290, 360 412, 705 430 L0 430 Z" fill="var(--green-dark)"/>
      <path d="M0 163 C 150 302, 360 414, 695 430 L0 430 Z" fill="var(--purple)"/>
      <path d="M0 185 C 160 322, 370 420, 685 430 L0 430 Z" fill="url(#back-green)"/>
    </svg>

    <p class="holder">Rosalind Pell BScHons, CPWRA, RGPC.</p>

    <p class="contact contact--phone">
      <svg class="contact__icon" viewBox="0 0 28 28" aria-hidden="true">
        <circle cx="14" cy="14" r="12.5" fill="none" stroke="var(--icon)" stroke-width="1.4"/>
        <path d="M9.5 8.2c1-.9 1.8-.6 2.3.3l1 1.8c.3.7.1 1.2-.5 1.7l-.7.5c.6 1.6 1.8 2.9 3.4 3.6l.6-.7c.5-.6 1-.7 1.7-.4l1.8 1c.9.5 1.1 1.3.3 2.2-1.3 1.4-3.3 1.2-5.4-.2-2.3-1.5-4-3.7-4.8-6-.6-1.7-.4-3 .3-3.8z" fill="var(--icon)"/>
      </svg>
      <span>07700 900482</span>
    </p>
    <p class="contact contact--email">
      <svg class="contact__icon" viewBox="0 0 28 28" aria-hidden="true">
        <rect x="2" y="7" width="24" height="15" rx="1.5" fill="none" stroke="var(--icon)" stroke-width="1.8"/>
        <path d="M2.5 7.8 L14 16 L25.5 7.8 M2.5 21.5 L11 14 M25.5 21.5 L17 14" fill="none" stroke="var(--icon)" stroke-width="1.6"/>
      </svg>
      <span>lumacrest@postvane.com</span>
    </p>

    <div class="brand brand--back">
      <span class="brand__dot"></span>
      <span class="brand__name">Rosa Pell Therapies</span>
    </div>
  </section>

</div>
</body>
</html>
```